Website design for Cambridge based systematic hedge fund

We have run previous craftmosaic competitions to design our company logo, business cards and the styling of our presentation deck (see attached files).
As the final step we are looking to get a website designed that is thematically consistent with these existing elements of our branding.
You can find some of our competitors websites below:
https://www.quelmarsh.example/
https://www.fenloor.example/
https://www.pyvart.example/
https://www.dulvet.example/
https://www.orbelmfunds.example/
https://www.valtrigo.example/
https://www.meskilfunds.example/home
We would like to have a website that works well on both mobile devices and desktops. Either just as one page that can be scrolled down, with links at the top that skips to certain sections, or a few separate pages that can be navigated by a top menu.
It should look professional, we are not after lots of animations or unnecessary transitions, and in particular the website must be smooth to navigate. We would like to avoid having peoples of people, we are happy to make use of elements from the presentation (for example the style of the cover slide, or the section slides with the faded bridge in the background), or 'financial' style images.
We would like to have the following sections for now. For some of these some example text has been provided, final text may change but it will be of similar length. For the other sections we are happy to just have template text for now. At the moment we are mainly interested to see styles/layouts as words can be added easily afterwards:
1) We will need a disclaimer pop up the first time someone visits the site (see for example the meskilfunds example).
2) Top page - company name, then in larger text "Bringing AI and Statistical Inference to Financial Markets", and somewhere in smaller text "Harlow Vectors is a quantitative asset manager with the singular focus of delivering algorithmic strategies that work"
3) "About us" section: will describe us as a company, details our approach, company values, and explains the company logo.
Example text:
"We deliver consistent alpha across liquid markets through the application of proprietary IP in Bayesian inference, machine learning and artificial intelligence. We are a multi-disciplinary team founded by experienced finance professionals from premier institutions, leading academics from the Thornbury Stellar Unit at Ashmere College and world-class software engineers.
Our logo portrays a sillhoute of the lattice walkway at Ashmere College. Our unique scientific approach allows us to bridge cutting-edge mathematical research and computing expertise with financial knowledge to bring algorithmns that work to liquid markets"
4) Hiring section, detailing our culture, what we are looking for.
Example text:
"We are always looking for exceptional talent to join our entrepreneurial team. We are looking for individuals who are creative thinkers, can demonstrate analytical rigour and are passionate about the intersection of science, finance and technology.
We prioritise having a company culture that promotes sharing ideas in a safe, collaborative research environment. We make sure that every member of the team has the oppertunity to explore their own ideas through weekly 'innovation time', and ensure that everyone gets the support they need to continue to grow as individuals within the company."
5) A section for news/press releases
6) Contact us area at the bottom with office location and email. We will need to list 3 addresses for our Cambridge, London and Singapore offices, along with a couple of contact emails or phone numbers
7) A client login button at the top that will take them to a different website (unrelated to this one).

```html
<!DOCTYPE html>
<html lang="en">
<head>
<meta charset="utf-8">
<title>Harlow Vectors</title>
<link rel="stylesheet" href="https://fonts.googleapis.com/css2?family=Montserrat:wght@500;600;700&family=Mulish:wght@400;600;700&display=swap">
<style>
:root{
  --navy:#073f72;
  --navy-deep:#0b2f5a;
  --blue:#4a8fd8;
  --btn:#5a98de;
  --ink:#333a44;
  --muted:#555d66;
  --light:#f1f1f1;
  --white:#ffffff;
}
*{box-sizing:border-box;margin:0;padding:0}
html,body{width:1200px;height:3236px;overflow:hidden}
body{font-family:"Mulish",sans-serif;color:var(--ink);background:var(--white);position:relative}
.abs{position:absolute}
.heading{font-family:"Montserrat",sans-serif;font-weight:700;text-transform:uppercase}
.btn{position:absolute;display:flex;align-items:center;justify-content:center;background:var(--btn);color:var(--white);font-family:"Montserrat",sans-serif;font-weight:600;font-size:15px;border-radius:3px;text-transform:uppercase}

/* hero */
.hero{position:absolute;left:0;top:0;width:1200px;height:580px;background:radial-gradient(ellipse at 50% 40%,#2a5c94 0%,#17406f 50%,#0c2a50 100%);color:var(--white)}
.brand-name{font-family:"Montserrat",sans-serif;font-weight:700;letter-spacing:1px}
.nav-brand{left:161px;top:50px;font-size:19px;color:var(--white)}
.nav{left:428px;top:55px;display:flex;gap:31px;font-family:"Montserrat",sans-serif;font-size:13.5px;font-weight:500}
.nav .active{font-weight:700}
.nav-divider{left:869px;top:42px;width:1px;height:48px;background:rgba(255,255,255,.35)}
.nav-phone{left:888px;top:50px;display:flex;align-items:center;gap:12px;font-family:"Montserrat",sans-serif;font-weight:700;font-size:15px}
.hero-title{left:0;width:1200px;top:222px;text-align:center;font-size:36px;line-height:48px;letter-spacing:.3px}
.hero-sub{left:0;width:1200px;top:320px;text-align:center;font-size:21px;line-height:30px;font-weight:600}

/* about */
.about-kicker{left:163px;top:669px;font-size:17px;color:var(--navy)}
.about-title{left:163px;top:695px;font-size:30px;color:var(--navy)}
.about-title span,.news-title span,.contact-title span{color:var(--blue)}
.about-text{left:163px;top:743px;width:390px;font-size:13.6px;line-height:24.5px;letter-spacing:.4px;color:var(--muted);text-align:justify}
.about-photo{left:585px;top:670px;width:454px;height:302px;border-radius:10px;background:linear-gradient(135deg,#e9ecef 0%,#cfd4d9 55%,#8d959d 100%)}
.feature{top:1048px;width:440px;height:100px}
.feature-icon{position:absolute;left:0;top:0;width:94px;height:94px;border-radius:50%;background:var(--white);box-shadow:0 6px 14px rgba(0,0,0,.15);display:flex;align-items:center;justify-content:center}
.feature-icon .core{width:78px;height:78px;border-radius:50%;background:var(--navy);display:flex;align-items:center;justify-content:center}
.feature h3{position:absolute;left:114px;top:4px;font-size:19px;color:var(--navy)}
.feature p{position:absolute;left:114px;top:32px;width:320px;font-size:13.4px;line-height:22px;color:var(--muted)}
.logo-mid{left:0;width:1200px;top:1222px;text-align:center;font-size:30px;color:var(--navy)}
.logo-caption{left:0;width:1200px;top:1278px;text-align:center;font-size:13.4px;line-height:22px;color:var(--muted)}

/* hiring */
.hiring{left:0;top:1408px;width:1200px;height:409px;background:var(--navy);color:var(--white)}
.hiring h2{position:absolute;left:0;width:1200px;top:84px;text-align:center;font-size:30px}
.hiring p{position:absolute;left:180px;width:840px;text-align:center;font-size:13.4px;line-height:22px}

/* news */
.news-title{left:0;width:1200px;top:1898px;text-align:center;font-size:31px;color:var(--navy)}
.card{position:absolute;top:1963px;width:277px;height:380px}
.card-photo{position:absolute;left:0;top:0;width:277px;height:218px;border-radius:6px 6px 0 0;background:linear-gradient(135deg,#cfc9c0,#6f6a63)}
.card-body{position:absolute;left:16px;top:189px;width:261px;height:191px;background:var(--white);box-shadow:0 4px 14px rgba(0,0,0,.12);border-radius:0 0 4px 4px}
.date{position:absolute;left:0;top:-22px;height:24px;padding:0 8px;background:var(--blue);color:var(--white);font-size:12px;font-weight:700;display:flex;align-items:center;gap:6px}
.card h4{position:absolute;left:18px;top:25px;width:230px;font-family:"Montserrat",sans-serif;font-weight:600;font-size:14.5px;line-height:19px;color:var(--ink)}
.card p{position:absolute;left:18px;top:75px;width:232px;font-size:13px;line-height:22px;color:var(--muted)}
.card a{position:absolute;left:18px;top:148px;font-family:"Montserrat",sans-serif;font-weight:700;font-size:13px;color:var(--blue);text-decoration:underline}

/* contact */
.contact-photo{left:0;top:2429px;width:510px;height:629px;background:linear-gradient(180deg,#3f7fc6 0%,#8cb5de 40%,#c8a66b 70%,#4a5a55 100%)}
.contact-panel{left:510px;top:2429px;width:690px;height:629px;background:var(--light)}
.contact-title{left:568px;top:2515px;font-size:30px;color:var(--navy)}
.office{position:absolute;width:230px}
.office h5{font-family:"Montserrat",sans-serif;font-weight:700;font-size:18px;color:var(--navy);text-transform:uppercase;margin-bottom:10px}
.line{position:relative;padding-left:23px;font-size:13.4px;line-height:21px;color:var(--muted);margin-bottom:12px}
.line b{font-family:"Montserrat",sans-serif;font-weight:600;font-size:13px;color:var(--ink);display:block}
.line svg{position:absolute;left:0;top:3px}
.logo-contact{left:817px;top:2895px;font-size:30px;color:var(--navy)}

/* footer */
.footer{left:0;top:3058px;width:1200px;height:178px;background:var(--navy);color:var(--white)}
.footer-nav{position:absolute;left:0;width:1200px;top:47px;display:flex;justify-content:center;gap:45px;font-family:"Montserrat",sans-serif;font-size:13.5px}
.footer-rule{position:absolute;left:161px;width:878px;top:99px;height:1px;background:rgba(255,255,255,.25)}
.copyright{position:absolute;left:0;width:1200px;top:137px;text-align:center;font-size:12.5px}
</style>
</head>
<body>

<header class="hero">
  <div class="abs brand-name nav-brand">HARLOW VECTORS</div>
  <nav class="abs nav"><span class="active">HOME</span><span>ABOUT US</span><span>HIRING</span><span>NEWS</span><span>CONTACT US</span></nav>
  <div class="abs nav-divider"></div>
  <div class="abs nav-phone">
    <svg width="26" height="26" viewBox="0 0 24 24" fill="none" stroke="#fff" stroke-width="1.4"><path d="M5 3h4l2 5-2.5 1.5a11 11 0 0 0 6 6L16 13l5 2v4a2 2 0 0 1-2 2A16 16 0 0 1 3 5a2 2 0 0 1 2-2z"/><path d="M15 3a6 6 0 0 1 6 6M15 6.5a2.5 2.5 0 0 1 2.5 2.5"/></svg>
    123-456-7890
  </div>
  <h1 class="abs heading hero-title">Bringing AI and Statistical Inference<br>to Financial Markets</h1>
  <p class="abs hero-sub">Harlow Vectors Is A Quantitative Asset Manager With The Singular Focus<br>Of Delivering Algorithmic Strategies That Work</p>
  <div class="btn" style="left:514px;top:402px;width:172px;height:41px">Call Us Today</div>
</header>

<section>
  <div class="abs heading about-kicker">About</div>
  <h2 class="abs heading about-title">Harlow <span>Vectors</span></h2>
  <p class="abs about-text">We deliver consistent alpha across liquid markets through the application of proprietary IP in Bayesian inference, machine learning and artificial intelligence. We are a multi-disciplinary team founded by experienced finance professionals from premier institutions, leading academics from the Thornbury Stellar Unit at Ashmere College and world-class software engineers.</p>
  <div class="btn" style="left:163px;top:931px;width:172px;height:41px">Call Us Today</div>
  <div class="abs about-photo" role="img" aria-label="Laptop with code on a bright office desk"></div>

  <div class="abs feature" style="left:163px">
    <div class="feature-icon"><div class="core">
      <svg width="40" height="40" viewBox="0 0 40 40" fill="none" stroke="#fff" stroke-width="1.6"><circle cx="20" cy="12" r="5"/><circle cx="12" cy="26" r="3.5"/><circle cx="28" cy="26" r="3.5"/><path d="M6 36v-3a6 6 0 0 1 12 0v3M22 36v-3a6 6 0 0 1 12 0v3"/></svg>
    </div></div>
    <h3 class="heading">Our Approach</h3>
    <p>Lorem ipsum dolor sit amet contetuer adipiscing elit sed diam nonummy nibh euismod tincidunt ut laoreet dolore magna aliquam.</p>
  </div>
  <div class="abs feature" style="left:623px">
    <div class="feature-icon"><div class="core">
      <svg width="40" height="40" viewBox="0 0 40 40" fill="none" stroke="#fff" stroke-width="1.6"><path d="M8 15l5-6h14l5 6-12 16z"/><path d="M8 15h24M16 9l-3 6 7 16 7-16-3-6"/></svg>
    </div></div>
    <h3 class="heading">Our Values</h3>
    <p>Lorem ipsum dolor sit amet contetuer adipiscing elit sed diam nonummy nibh euismod tincidunt ut laoreet dolore magna aliquam.</p>
  </div>

  <div class="abs brand-name logo-mid">HARLOW VECTORS</div>
  <p class="abs logo-caption">Our unique scientific approach allows us to bridge cutting-edge mathematical research and computing<br>expertise with financial knowledge to bring algorithmns that work to liquid markets</p>
</section>

<section class="abs hiring">
  <h2 class="heading">Hiring</h2>
  <p style="top:130px">We are always looking for exceptional talent to join our entrepreneurial team. We are looking for individuals who are creative thinkers, can demonstrate analytical rigour and are passionate about the intersection of science, finance and technology.</p>
  <p style="top:186px">We prioritise having a company culture that promotes sharing ideas in a safe, collaborative research environment. We make sure that every member of the team has the opportunity to explore their own ideas through weekly 'innovation time', and ensure that everyone gets the support they need to continue to grow as individuals within the company.</p>
  <div class="btn" style="left:514px;top:278px;width:172px;height:41px">Join Our Team</div>
</section>

<section>
  <h2 class="abs heading news-title">Latest <span>News</span></h2>
  <svg class="abs" style="left:88px;top:2158px" width="34" height="16" viewBox="0 0 34 16" fill="none" stroke="#073f72" stroke-width="1.8"><path d="M33 8H2M9 1L2 8l7 7"/></svg>
  <svg class="abs" style="left:1070px;top:2158px" width="34" height="16" viewBox="0 0 34 16" fill="none" stroke="#073f72" stroke-width="1.8"><path d="M1 8h31M25 1l7 7-7 7"/></svg>

  <article class="card" style="left:161px">
    <div class="card-photo" role="img" aria-label="Paper chart and ruler on a wooden table"></div>
    <div class="card-body">
      <div class="date"><svg width="12" height="12" viewBox="0 0 12 12" fill="none" stroke="#fff"><rect x="1" y="2" width="10" height="9"/><path d="M1 5h10M4 1v2M8 1v2"/></svg>28 Aug, 2021</div>
      <h4>Lorem Ipsum Dolor Conetuer Adipiscig Elit Sed.</h4>
      <p>Ut wisi enim ad minim veniam uis norud exerci tation ullaper suscipit lobotis nisl ut aliquip ex ea.</p>
      <a>READ MORE</a>
    </div>
  </article>
  <article class="card" style="left:462px">
    <div class="card-photo" role="img" aria-label="Hands writing notes beside a laptop" style="background:linear-gradient(135deg,#9fb0b3,#4f5d60)"></div>
    <div class="card-body">
      <div class="date"><svg width="12" height="12" viewBox="0 0 12 12" fill="none" stroke="#fff"><rect x="1" y="2" width="10" height="9"/><path d="M1 5h10M4 1v2M8 1v2"/></svg>28 Aug, 2021</div>
      <h4>Lorem Ipsum Dolor Conetuer Adipiscig Elit Sed.</h4>
      <p>Ut wisi enim ad minim veniam uis norud exerci tation ullaper suscipit lobotis nisl ut aliquip ex ea.</p>
      <a>READ MORE</a>
    </div>
  </article>
  <article class="card" style="left:762px">
    <div class="card-photo" role="img" aria-label="Phone showing market data over a keyboard" style="background:linear-gradient(135deg,#6d4a35,#2c2a2c)"></div>
    <div class="card-body">
      <div class="date"><svg width="12" height="12" viewBox="0 0 12 12" fill="none" stroke="#fff"><rect x="1" y="2" width="10" height="9"/><path d="M1 5h10M4 1v2M8 1v2"/></svg>28 Aug, 2021</div>
      <h4>Lorem Ipsum Dolor Conetuer Adipiscig Elit Sed.</h4>
      <p>Ut wisi enim ad minim veniam uis norud exerci tation ullaper suscipit lobotis nisl ut aliquip ex ea.</p>
      <a>READ MORE</a>
    </div>
  </article>
</section>

<section>
  <div class="abs contact-photo" role="img" aria-label="Clock tower and riverside parliament buildings under blue sky"></div>
  <div class="abs contact-panel"></div>
  <h2 class="abs heading contact-title">Contact <span>Us</span></h2>

  <div class="office" style="left:568px;top:2578px">
    <h5>Cambridge Office</h5>
    <div class="line"><svg width="12" height="15" viewBox="0 0 12 15" fill="#4a8fd8"><path d="M6 0a6 6 0 0 1 6 6c0 4-6 9-6 9S0 10 0 6a6 6 0 0 1 6-6zm0 3.5a2.5 2.5 0 1 0 0 5 2.5 2.5 0 0 0 0-5z"/></svg>123 Lorem ipsum dolor sit amet, consectetuer.</div>
    <div class="line"><svg width="14" height="14" viewBox="0 0 24 24" fill="#4a8fd8"><path d="M5 2h4l2 5-2.5 1.5a11 11 0 0 0 7 7L17 13l5 2v4a2 2 0 0 1-2 2A18 18 0 0 1 3 4a2 2 0 0 1 2-2z"/></svg><b>PHONE</b>123-456-7890</div>
    <div class="line"><svg width="15" height="11" viewBox="0 0 15 11" fill="#4a8fd8"><path d="M0 0h15v11H0z"/><path d="M0 0l7.5 6L15 0" stroke="#f1f1f1" fill="none"/></svg><b>EMAIL</b>info@harlowvectors.example</div>
  </div>
  <div class="office" style="left:817px;top:2578px">
    <h5>London Office</h5>
    <div class="line"><svg width="12" height="15" viewBox="0 0 12 15" fill="#4a8fd8"><path d="M6 0a6 6 0 0 1 6 6c0 4-6 9-6 9S0 10 0 6a6 6 0 0 1 6-6zm0 3.5a2.5 2.5 0 1 0 0 5 2.5 2.5 0 0 0 0-5z"/></svg>123 Lorem ipsum dolor sit amet, consectetuer.</div>
    <div class="line"><svg width="14" height="14" viewBox="0 0 24 24" fill="#4a8fd8"><path d="M5 2h4l2 5-2.5 1.5a11 11 0 0 0 7 7L17 13l5 2v4a2 2 0 0 1-2 2A18 18 0 0 1 3 4a2 2 0 0 1 2-2z"/></svg><b>PHONE</b>123-456-7890</div>
    <div class="line"><svg width="15" height="11" viewBox="0 0 15 11" fill="#4a8fd8"><path d="M0 0h15v11H0z"/><path d="M0 0l7.5 6L15 0" stroke="#f1f1f1" fill="none"/></svg><b>EMAIL</b>info@harlowvectors.example</div>
  </div>
  <div class="office" style="left:568px;top:2799px">
    <h5>Singapore Office</h5>
    <div class="line"><svg width="12" height="15" viewBox="0 0 12 15" fill="#4a8fd8"><path d="M6 0a6 6 0 0 1 6 6c0 4-6 9-6 9S0 10 0 6a6 6 0 0 1 6-6zm0 3.5a2.5 2.5 0 1 0 0 5 2.5 2.5 0 0 0 0-5z"/></svg>123 Lorem ipsum dolor sit amet, consectetuer.</div>
    <div class="line"><svg width="14" height="14" viewBox="0 0 24 24" fill="#4a8fd8"><path d="M5 2h4l2 5-2.5 1.5a11 11 0 0 0 7 7L17 13l5 2v4a2 2 0 0 1-2 2A18 18 0 0 1 3 4a2 2 0 0 1 2-2z"/></svg><b>PHONE</b>123-456-7890</div>
    <div class="line"><svg width="15" height="11" viewBox="0 0 15 11" fill="#4a8fd8"><path d="M0 0h15v11H0z"/><path d="M0 0l7.5 6L15 0" stroke="#f1f1f1" fill="none"/></svg><b>EMAIL</b>info@harlowvectors.example</div>
  </div>
  <div class="abs brand-name logo-contact">HARLOW VECTORS</div>
</section>

<footer class="abs footer">
  <nav class="footer-nav"><span>HOME</span><span>ABOUT US</span><span>HIRING</span><span>NEWS</span><span>CONTACT US</span></nav>
  <div class="footer-rule"></div>
  <p class="copyright">Copyright © 2021 HARLOW VECTORS. All Rights Reserved.</p>
</footer>

</body>
</html>
```